Copper Vale Tattoo

Business card / Appointment card in one

Ive attached the new logo along with a simple format of what I would like written out on the back! Would like a clean/ modern style font to be used! I also attached the current card for a reference of style!

The colors of this would be either white and gold lettering or black with gold lettering.

Email - CopperValeNB@inkmail.example
Ph # 555-482-9073

The message at bottom of back - All cancellations or No Call No Shows within 48 hours of appointment time will result in a forfeit of deposit.

Small block avail (if card is black) to write in appointment date/time

Target Market(s)

Card for Tattoo shop

Contact Information for Business Card

in project description area!

Font styles to use
Sans Serif

Requirements
Must have
• Please refer to current business card photos that were attached as well!
Nice to have
• Looking for blacks, greys and gold for color scheme

```html
<!DOCTYPE html>
<html lang="en">
<head>
<meta charset="utf-8">
<title>Copper Vale Tattoo – Business &amp; Appointment Card</title>
<link rel="stylesheet" href="https://fonts.googleapis.com/css2?family=Lato:wght@400;700;900&display=swap">
<style>
  :root {
    --backdrop: #2a2a2d;
    --card-black: #0b0b0b;
    --panel-black: #141414;
    --border-dark: #1c1c1c;
    --border-mid: #4a4a4a;
    --frame-grey: #7d7d7d;
    --gold: #c9a43a;
    --white: #ffffff;
    --ink: #111111;
  }
  * { box-sizing: border-box; margin: 0; padding: 0; }
  html, body {
    width: 1200px;
    height: 803px;
    overflow: hidden;
    background: var(--backdrop);
    font-family: "Lato", sans-serif;
  }
  .canvas {
    position: relative;
    width: 1200px;
    height: 803px;
  }

  /* Front of card */
  .card-front {
    position: absolute;
    left: 90px;
    top: 241px;
    width: 560px;
    height: 320px;
    background: var(--card-black);
    box-shadow: 0 10px 30px rgba(0,0,0,.5);
    display: flex;
    align-items: center;
    justify-content: center;
    gap: 14px;
  }
  .brand-mark {
    width: 14px;
    height: 14px;
    background: var(--gold);
  }
  .brand-name {
    font-weight: 700;
    font-size: 30px;
    letter-spacing: 3px;
    color: var(--gold);
    text-transform: uppercase;
  }

  /* Back of card */
  .card-back {
    position: absolute;
    left: 760px;
    top: 121px;
    width: 340px;
    height: 560px;
    padding: 24px;
    box-shadow: 0 10px 30px rgba(0,0,0,.5);
    display: flex;
    flex-direction: column;
  }
  .border-fill {
    position: absolute;
    inset: 0;
    background: linear-gradient(135deg, var(--border-dark) 0%, var(--border-mid) 50%, var(--border-dark) 100%);
  }
  .info-panel,
  .appointment-block { position: relative; }

  .info-panel {
    flex: 0 0 262px;
    background: linear-gradient(180deg, #000 0%, var(--panel-black) 100%);
    border: 3px solid var(--frame-grey);
    border-bottom: none;
    padding: 30px 18px 0;
    color: var(--white);
  }
  .shop-name {
    font-weight: 900;
    font-size: 36px;
    line-height: 1.05;
    text-align: center;
    letter-spacing: 0.5px;
  }
  .shop-sub {
    font-weight: 700;
    font-size: 20px;
    letter-spacing: 4px;
    text-transform: uppercase;
    text-align: center;
    margin: 4px 0 30px;
  }
  .contact {
    font-size: 16px;
    line-height: 1.6;
  }
  .contact-phone { font-size: 20px; }

  .appointment-block {
    flex: 1;
    background: var(--white);
    border: 3px solid var(--frame-grey);
    padding: 18px 18px 14px;
    color: var(--ink);
  }
  .appointment-title {
    font-weight: 700;
    font-size: 18px;
    text-align: right;
    margin-bottom: 12px;
  }
  .field {
    display: flex;
    align-items: flex-end;
    gap: 8px;
    font-size: 14px;
    margin-bottom: 18px;
  }
  .field-line {
    flex: 1;
    border-bottom: 1.5px solid var(--ink);
    height: 1px;
  }
  .policy {
    font-size: 14px;
    line-height: 1.35;
    text-align: center;
    margin-top: 20px;
  }
</style>
</head>
<body>
<main class="canvas">
  <section class="card-front" aria-label="Card front">
    <span class="brand-mark"></span>
    <span class="brand-name">Copper Vale Tattoo</span>
  </section>

  <section class="card-back" aria-label="Card back">
    <div class="border-fill" role="img" aria-label="Decorative diagonal grey and black striped border"></div>
    <div class="info-panel">
      <div class="shop-name">Copper Vale</div>
      <div class="shop-sub">Tattoo</div>
      <p class="contact">CopperValeNB@inkmail.example</p>
      <p class="contact contact-phone">№ 555-482-9073</p>
    </div>
    <div class="appointment-block">
      <div class="appointment-title">Appointment</div>
      <div class="field"><span>Time</span><span class="field-line"></span></div>
      <div class="field"><span>Date</span><span class="field-line"></span></div>
      <p class="policy">All cancellations or No Call No Shows within 48 hours of appointment time will result in a forfeit of deposit.</p>
    </div>
  </section>
</main>
</body>
</html>
```